Quill Refrigeration. Refrigeration and air conditioning specialists.

We need a website to promote our business. We would a modern simple design using the colours from our logo and black. We want it to be fun but proffesional.

Target Market(s)

Commercial

Number of Pages Required

4 page

Requirements
Must have
• Home Page, About Us, Services and Contact Us.
• 24/7 365 days service available.
• Quill Refrigeration's dedicated team specialises in commercial refrigeration and air conditioning equipment.
• Based in Harbourvale, we cover Westbay Metro and surrounding areas.
Nice to have
• KNOWLEDGE . EXPERIENCE . PASSION in bold.
• Our experienced and highly trained technicians provide extensive knowledge and exceptional skills for your commercial refrigeration and air conditioning requirements.
• Pictures of commercial refrigeration.
Should not have
• No mention of domestic services.

```html
<!DOCTYPE html>
<html lang="en">
<head>
<meta charset="utf-8">
<title>Quill Refrigeration</title>
<link href="https://fonts.googleapis.com/css2?family=Roboto:wght@300;400;500;700&family=Roboto+Condensed:wght@400;700&display=swap" rel="stylesheet">
<style>
:root{
  --purple:#3b2160;
  --purple-deep:#321a55;
  --lime:#a3f060;
  --lime-dark:#6cbf2a;
  --ink:#222;
  --body:#666;
  --grey-bg:#efefef;
  --footer:#2e2e2e;
  --white:#fff;
}
*{box-sizing:border-box;margin:0;padding:0}
html,body{width:1200px;height:4138px;overflow:hidden}
body{position:relative;background:var(--white);font-family:"Roboto",sans-serif;color:var(--ink)}
.abs{position:absolute}
.center{text-align:center}

/* top bar */
.topbar{left:0;top:0;width:1200px;height:36px;background:var(--white)}
.topbar .call{left:710px;top:9px;color:var(--ink);font-size:14px;display:flex;align-items:center;gap:8px}
.topbar .call b{color:var(--lime-dark);font-weight:500}
.topbar .social{left:996px;top:11px;display:flex;gap:18px}
.topbar .social span{width:14px;height:14px;border-radius:50%;background:var(--lime-dark)}

/* header */
.header{left:0;top:36px;width:1200px;height:116px;background:var(--white);border-bottom:6px solid var(--lime)}
.brand{left:91px;top:24px;color:var(--lime-dark);font-family:"Roboto Condensed",sans-serif;font-weight:700;font-size:30px;line-height:34px;display:flex;align-items:center;gap:10px}
.brand i{width:22px;height:22px;background:var(--lime-dark);display:block}
.nav{left:376px;top:46px;display:flex;font-size:15px;color:#444}
.nav a{color:#444;text-decoration:none;width:154px;text-align:center;position:relative}
.nav a+a::before{content:"";position:absolute;left:0;top:3px;height:14px;border-left:1px solid #999}
.badge{left:1000px;top:18px;display:flex;flex-direction:column;align-items:center}
.badge span{width:34px;height:34px;border-radius:50%;background:var(--purple)}
.badge b{font-size:16px;color:var(--ink);margin-top:4px;white-space:nowrap}
.badge b small{font-size:11px}

/* hero */
.hero{left:0;top:152px;width:1200px;height:690px;background:linear-gradient(180deg,#8a8f94 0%,#6e7378 45%,#5c6064 100%);border-bottom:6px solid var(--lime)}
.hero::after{content:"";position:absolute;inset:0;background:rgba(20,20,30,.35)}
.hero-text{left:0;top:170px;width:1200px;z-index:2;color:var(--white)}
.hero-text .lead{font-size:44px;font-weight:300;line-height:52px}
.hero-text h1{font-family:"Roboto Condensed",sans-serif;font-weight:700;font-size:58px;line-height:68px;letter-spacing:.5px}
.hero-text .kep{font-family:"Roboto Condensed",sans-serif;font-weight:700;font-size:46px;color:var(--lime);letter-spacing:1.5px;line-height:56px}
.btn-lime{background:var(--lime);color:var(--purple);font-weight:500;border:none;font-size:20px;font-family:"Roboto Condensed",sans-serif}
.hero .more{left:505px;top:463px;width:193px;height:42px;z-index:2;border-radius:3px}
.dots{left:577px;top:624px;z-index:2;display:flex;gap:10px}
.dots span{width:10px;height:10px;border-radius:50%;border:2px solid var(--white)}
.dots span:first-child{background:var(--white)}

/* section titles */
.title{left:0;width:1200px;text-align:center;font-size:34px;font-weight:500;color:var(--purple)}
.title::after{content:"";display:block;width:60px;height:2px;background:#bbb;margin:14px auto 0}
.intro{left:0;width:1200px;text-align:center;font-size:13px;line-height:23px;color:var(--body)}

/* about */
.about-photo{left:124px;top:1104px;width:455px;height:281px;background:linear-gradient(135deg,#8c8a80,#5d6168 60%,#b7b3a6)}
.about-copy{left:621px;top:1100px;width:455px;font-size:12.5px;line-height:21px;color:var(--body)}
.about-copy p+p{margin-top:20px}

/* services */
.services{left:0;top:1504px;width:1200px;height:932px;background:var(--grey-bg)}
.card{width:261px;height:254px;border:2px solid #c9c9c9;background:var(--grey-bg);text-align:center}
.card .num{display:inline-block;width:48px;height:48px;background:var(--purple);color:var(--white);font-size:30px;line-height:48px;margin-top:50px}
.card h3{font-size:16px;font-weight:700;color:var(--purple);margin-top:12px}
.card p{font-size:12px;line-height:18px;color:var(--body);width:190px;margin:14px auto 0}
.arrow{width:30px;height:50px}

/* contact */
.contact{left:0;top:2436px;width:1200px;height:618px;background:var(--purple)}
.lbl{color:var(--white);font-size:14px}
.lbl sup{color:var(--lime);font-size:14px;margin-left:4px}
.field{background:var(--white)}
.check{color:var(--white);font-size:14px;display:flex;align-items:center;gap:10px}
.check i{width:16px;height:16px;background:var(--white);display:block}
.submit{left:532px;top:2919px;width:136px;height:33px;border-radius:3px;font-size:18px}

/* testimonials */
.quote{width:381px;height:130px;border:2px solid #ccc;background:var(--white);padding:28px 24px 0}
.quote .mark{position:absolute;left:24px;top:-12px;font-size:48px;line-height:40px;color:var(--lime);font-family:"Roboto Condensed",sans-serif;font-weight:700;background:var(--white);padding:0 2px}
.quote h4{font-size:14px;font-weight:700;color:var(--purple)}
.quote p{font-size:12px;line-height:18px;color:var(--body);margin-top:8px}
.person{display:flex;align-items:center;gap:12px}
.person span{width:46px;height:46px;border-radius:50%;background:#9a9aa6}
.person b{display:block;font-size:14px;color:var(--purple)}
.person small{font-size:10px;color:var(--body)}

/* newsletter */
.newsletter{left:0;top:3587px;width:1200px;height:151px;background:var(--lime)}
.newsletter h2{left:174px;top:60px;font-size:24px;font-weight:500;color:var(--purple)}
.newsletter .input{left:381px;top:55px;width:507px;height:49px;background:var(--white)}
.newsletter .sub{left:888px;top:55px;width:127px;height:49px;background:var(--purple);color:var(--white);font-size:14px;font-weight:700;display:flex;align-items:center;justify-content:center}

/* footer */
.footer{left:0;top:3738px;width:1200px;height:318px;background:var(--footer)}
.footer .brand{left:110px;top:126px;color:var(--white);font-size:21px;line-height:26px;gap:8px}
.footer .brand i{background:var(--white);width:16px;height:16px}
.fhead{font-size:16px;font-weight:700;color:var(--lime)}
.fline{color:var(--white);font-size:14px;line-height:20px}
.fline b{color:var(--lime);font-weight:700;font-size:13px}
.flinks{color:var(--white);font-size:14px;line-height:32px}
.finput{background:var(--white);color:#999;font-size:13px;padding:12px 10px}
.send{background:var(--lime);color:var(--purple);font-weight:700;font-size:14px;display:flex;align-items:center;justify-content:center}
.copyright{left:0;top:4056px;width:1200px;height:82px;background:var(--purple-deep);color:#cfc6dc;font-size:12px;text-align:center;line-height:82px}
</style>
</head>
<body>

<div class="abs topbar">
  <div class="abs call">
    <svg width="18" height="18" viewBox="0 0 24 24"><circle cx="12" cy="12" r="12" fill="#6cbf2a"/><path d="M8.5 6.5l2 2-1.2 1.6c.8 1.7 2 2.9 3.6 3.6l1.6-1.2 2 2-1.5 1.8c-4.2-.4-7.9-4.1-8.3-8.3z" fill="#fff"/></svg>
    <span>Call Us Free <b>1-888-555-0142</b></span>
  </div>
  <div class="abs social"><span></span><span></span><span></span><span></span></div>
</div>

<header class="abs header">
  <div class="abs brand"><i></i>Quill Refrigeration</div>
  <nav class="abs nav">
    <a href="#">Home</a><a href="#">About Us</a><a href="#">Services</a><a href="#">Contact Us</a>
  </nav>
  <div class="abs badge"><span></span><b>24/7 <small>365 DAYS</small></b></div>
</header>

<section class="abs hero" role="img" aria-label="Photo of rooftop commercial air conditioning condenser units">
  <div class="abs hero-text center">
    <p class="lead">Our dedicated team specialises in</p>
    <h1>COMMERCIAL REFRIGERATION &amp;<br>AIR CONDITIONING EQUIPMENT</h1>
    <p class="kep">KNOWLEDGE • EXPERIENCE • PASSION</p>
  </div>
  <button class="abs btn-lime more">KNOW MORE</button>
  <div class="abs dots"><span></span><span></span><span></span></div>
</section>

<h2 class="abs title" style="top:938px">About us</h2>
<p class="abs intro" style="top:1014px">Quill Refrigeration's dedicated team specialises in commercial refrigeration and air conditioning equipment.<br>Based in Harbourvale, we cover Westbay Metro and surrounding areas.</p>
<div class="abs about-photo" role="img" aria-label="Photo of a technician servicing a commercial refrigeration unit"></div>
<div class="abs about-copy">
  <p>Lorem ipsum dolor sit amet, consectetur adipiscing elit. Quid autem habent admirationis, cum prope accesseris? An hoc usque quaque, aliter in vita? Non igitur de improbo, sed de callido improbo quaerimus, qualis Q. Nam quibus rebus efficiuntur voluptates, eae non sunt in potestate sapientis. Negare non possum. Haec mox optimum esse propter desperationem sapientiae, illi propter spem vivere. Quid enim me prohiberet Epicureum esse, si probarem, quae ille diceret? Qui-vere falsone, quaerere mittimus dicitur oculis se privasse.</p>
  <p>Varietates autem iniurasque fortunae facile veteres philosophorum praeceptis instituta vita superabat. Et quod est munus, quod opus sapientiae? Non modo carum sibi quemque, verum etiam vehementer carum esse? Tu enim ista lenius, hic Stoicorum more nos vexat. Collatio igitur ista te nihil iuvat. Videamus animi partes, quarum est conspectus illustrior.</p>
</div>

<section class="abs services"></section>
<h2 class="abs title" style="top:1570px">Our Services</h2>
<p class="abs intro" style="top:1656px">Whether you wish to cool, store or display food and drink, we have a wide range of commercial refrigerator services catering to various small and large scale industries.<br>We specialize in wide range of commercial refrigeration operations and maintenance services to ensure efficient functioning of the systems.</p>

<svg class="abs arrow" style="left:52px;top:2022px" viewBox="0 0 30 50"><path d="M24 2L4 25l20 23" fill="none" stroke="#999" stroke-width="2"/></svg>
<svg class="abs arrow" style="left:1117px;top:2022px" viewBox="0 0 30 50"><path d="M6 2l20 23L6 48" fill="none" stroke="#999" stroke-width="2"/></svg>

<div class="abs card" style="left:146px;top:1760px"><span class="num">01</span><h3>Commercial Freezer</h3><p>Lorem ipsum dolor sit amet, consectetur adipiscing elit. Morbi auctor ullamcorper congue.</p></div>
<div class="abs card" style="left:472px;top:1760px"><span class="num">02</span><h3>Walk In Cooler</h3><p>Lorem ipsum dolor sit amet, consectetur adipiscing elit. Morbi auctor ullamcorper congue.</p></div>
<div class="abs card" style="left:797px;top:1760px"><span class="num">03</span><h3>Kitchen Refrigeration</h3><p>Lorem ipsum dolor sit amet, consectetur adipiscing elit. Morbi auctor ullamcorper congue.</p></div>
<div class="abs card" style="left:146px;top:2077px"><span class="num">04</span><h3>Glass Door Merchandiser</h3><p>Lorem ipsum dolor sit amet, consectetur adipiscing elit. Morbi auctor ullamcorper congue.</p></div>
<div class="abs card" style="left:472px;top:2077px"><span class="num">05</span><h3>Commercial Freezer</h3><p>Lorem ipsum dolor sit amet, consectetur adipiscing elit. Morbi auctor ullamcorper congue.</p></div>
<div class="abs card" style="left:797px;top:2077px"><span class="num">06</span><h3>Ice machines</h3><p>Lorem ipsum dolor sit amet, consectetur adipiscing elit. Morbi auctor ullamcorper congue.</p></div>

<section class="abs contact"></section>
<h2 class="abs title" style="top:2511px;color:var(--lime)">Contact Us</h2>
<span class="abs lbl" style="left:152px;top:2621px">Name<sup>*</sup></span>
<div class="abs field" style="left:152px;top:2649px;width:394px;height:34px"></div>
<span class="abs lbl" style="left:152px;top:2706px">Email<sup>*</sup></span>
<div class="abs field" style="left:152px;top:2734px;width:394px;height:36px"></div>
<span class="abs lbl" style="left:152px;top:2793px">Phone</span>
<div class="abs field" style="left:152px;top:2817px;width:394px;height:36px"></div>
<span class="abs lbl" style="left:673px;top:2621px">Description</span>
<div class="abs field" style="left:673px;top:2649px;width:395px;height:129px"></div>
<span class="abs lbl" style="left:673px;top:2793px;font-size:13px;color:#cfc6dc">+ Required</span>
<div class="abs check" style="left:673px;top:2827px"><i></i>I have read the Disclaimer and Privacy Policy</div>
<button class="abs btn-lime submit">SUBMIT</button>

<h2 class="abs title" style="top:3159px">Client Testimonials</h2>
<div class="abs quote" style="left:188px;top:3272px"><span class="mark">“</span><h4>Lorem ipsum dolor</h4><p>Lorem ipsum dolor sit amet, consectetur adipiscing elit. Quid autem habent admirationis, cum prope accesseris? An hoc usque quaque, aliter in vita?</p></div>
<div class="abs quote" style="left:632px;top:3272px"><span class="mark">“</span><h4>Lorem ipsum dolor</h4><p>Lorem ipsum dolor sit amet, consectetur adipiscing elit. Quid autem habent admirationis, cum prope accesseris? An hoc usque quaque, aliter in vita?</p></div>
<div class="abs person" style="left:212px;top:3415px"><span role="img" aria-label="Client portrait"></span><div><b>CLARA BENTON</b><small>Lorem ipsum dolor</small></div></div>
<div class="abs person" style="left:644px;top:3415px"><span role="img" aria-label="Client portrait"></span><div><b>MARCUS HALE</b><small>Lorem ipsum dolor</small></div></div>

<section class="abs newsletter">
  <h2 class="abs">NEWSLETTER</h2>
  <div class="abs input"></div>
  <div class="abs sub">SUBSCRIBE</div>
</section>

<footer class="abs footer">
  <div class="abs brand"><i></i>Quill Refrigeration</div>
  <h3 class="abs fhead" style="left:359px;top:70px">CONTACT US</h3>
  <svg class="abs" style="left:357px;top:105px" width="20" height="26" viewBox="0 0 20 26"><path d="M10 0C4.5 0 0 4.3 0 9.6 0 16.8 10 26 10 26s10-9.2 10-16.4C20 4.3 15.5 0 10 0z" fill="#a3f060"/><circle cx="10" cy="9.5" r="3.6" fill="#2e2e2e"/></svg>
  <div class="abs fline" style="left:393px;top:103px"><b>ADDRESS</b><br>48 Fernleigh Road<br>Harbourvale 6027</div>
  <svg class="abs" style="left:357px;top:188px" width="20" height="20" viewBox="0 0 24 24"><path d="M5 2l4 4-2.2 2.8c1.4 3.2 3.9 5.6 7.1 7.1L16.7 14l4 4-3 3.5C9.8 20.8 3.2 14.2 2.5 6.3z" fill="#a3f060"/></svg>
  <div class="abs fline" style="left:393px;top:186px"><b>PHONE NUMBER</b><br>1-888-555-0142</div>
  <h3 class="abs fhead" style="left:626px;top:70px">ABOUT</h3>
  <div class="abs flinks" style="left:628px;top:108px">Home<br>About Us<br>Services<br>Contact us</div>
  <h3 class="abs fhead" style="left:792px;top:70px">GET IN TOUCH</h3>
  <div class="abs finput" style="left:795px;top:105px;width:151px;height:39px">Name</div>
  <div class="abs finput" style="left:952px;top:105px;width:152px;height:39px">Phone</div>
  <div class="abs finput" style="left:795px;top:152px;width:309px;height:36px;padding-top:10px">Email address</div>
  <div class="abs send" style="left:795px;top:207px;width:129px;height:36px">SEND</div>
</footer>

<div class="abs copyright">© 2018 quillrefrigeration All Right Reserved</div>

</body>
</html>
```